I would like to incoroporate some of the photos attached for a design on a 4x6 postcard. This is for a design/build company called Tom Brenner Garden Design. We design the landscape or garden and install it. The phone number, I want to use is 555-316-2087. I want the design to make someone want to call imediately for a landscape makeover. I have attached several photos of work we have done. I would rather not use other images of other peoples work, but am open to ideas. Want to keep wording to a mininum since the name pretty much says it all and focus on a creative design incorporating garden design photos.
I would like at the bottom of the page something that says something to the effect of: "Find some of our completed design under YardCraft on Gardenly or yardcraft.example
The post card will be two sided

```html
<!DOCTYPE html>
<html lang="en">
<head>
<meta charset="utf-8">
<title>Tom Brenner Garden Design – Postcard</title>
<link rel="stylesheet" href="https://fonts.googleapis.com/css2?family=Arimo:wght@400;700&family=Libre+Baskerville:wght@700&display=swap">
<style>
  :root {
    --page: #ffffff;
    --front-bg: #e4e2df;
    --header-bg: #5b5551;
    --back-bg: #f1eee7;
    --band: #4a4440;
    --ink: #111111;
    --muted: #6a6663;
    --white: #ffffff;
    --leaf: #6fb43f;
    --logo-ink: #2d2a28;
  }
  * { box-sizing: border-box; margin: 0; padding: 0; }
  html, body { width: 877px; height: 1200px; overflow: hidden; background: var(--page); }
  body { position: relative; font-family: "Arimo", Arial, sans-serif; }

  .side { position: absolute; left: 0; width: 877px; }
  .side--front { top: 0; height: 614px; background: var(--front-bg); border-bottom: 2px solid #cfccc8; }
  .side--back { top: 622px; height: 578px; background: var(--back-bg); }

  .header {
    position: absolute; left: 20px; top: 20px; width: 833px; height: 76px;
    background: var(--header-bg);
  }
  .brand {
    position: absolute; background: var(--white);
    border: 2px solid #8f8a86; border-radius: 16px;
    display: flex; align-items: center; gap: 14px; padding: 0 16px;
  }
  .header .brand { left: 4px; top: 5px; width: 260px; height: 66px; }
  .brand__name { color: var(--logo-ink); font-weight: 700; line-height: 1.05; }
  .header .brand__name { font-size: 21px; }
  .brand__dot { flex: none; border-radius: 50%; background: var(--leaf); }
  .header .brand__dot { width: 34px; height: 34px; }

  .header__note {
    position: absolute; left: 300px; top: 13px;
    color: var(--white); font-size: 22px; line-height: 1.22;
  }

  .photo { position: absolute; border-radius: 14px; }
  .photo--driveway { left: 26px; top: 106px; width: 396px; height: 296px;
    background: linear-gradient(160deg, #4f6b3a 0%, #7a8a5a 40%, #b84a5a 70%, #9fa24a 100%); }
  .photo--patio { left: 434px; top: 106px; width: 419px; height: 192px;
    background: linear-gradient(150deg, #2f3a22 0%, #5c5a3e 45%, #a38d72 70%, #3a4a2a 100%); }
  .photo--leaves { left: 434px; top: 309px; width: 419px; height: 93px;
    background: linear-gradient(90deg, #c7457a 0%, #e7a6c0 35%, #4d7a3a 55%, #d65a8e 100%); }
  .photo--path { left: 26px; top: 416px; width: 827px; height: 181px;
    background: linear-gradient(100deg, #5a4a3c 0%, #9db83e 25%, #c6283a 45%, #d8d2c4 55%, #a8c24a 75%, #5b4838 100%); }

  .side--back .brand { left: 20px; top: 48px; width: 311px; height: 96px; border-radius: 20px; }
  .side--back .brand__name { font-size: 26px; }
  .side--back .brand__dot { width: 46px; height: 46px; }

  .back__note {
    position: absolute; left: 28px; top: 178px;
    color: var(--muted); font-size: 19px; line-height: 1.3;
  }
  .divider { position: absolute; left: 396px; top: 32px; width: 7px; height: 322px;
    background: var(--leaf); border-radius: 4px; }

  .call-band {
    position: absolute; left: 0; top: 393px; width: 877px; height: 84px;
    background: var(--band); display: flex; align-items: center; justify-content: center;
  }
  .call-band__phone {
    font-family: "Libre Baskerville", Georgia, serif; font-weight: 700;
    color: var(--white); font-size: 57px; letter-spacing: 1px;
  }
  .tagline {
    position: absolute; left: 0; top: 492px; width: 877px; text-align: center;
    color: var(--ink); font-weight: 700; font-size: 26px; line-height: 1.35;
  }
</style>
</head>
<body>
  <section class="side side--front">
    <header class="header">
      <div class="brand">
        <span class="brand__name">Tom Brenner<br>Garden Design</span>
        <span class="brand__dot"></span>
      </div>
      <p class="header__note">Find some of our completed designs<br>at YardCraft on Gardenly or yardcraft.example</p>
    </header>
    <div class="photo photo--driveway" role="img" aria-label="Photo of a home driveway bordered by red and pink flower beds and lime green foliage"></div>
    <div class="photo photo--patio" role="img" aria-label="Photo of an evening garden patio with an outdoor sofa, rug and stone fireplace"></div>
    <div class="photo photo--leaves" role="img" aria-label="Close-up photo of pink and green caladium leaves with a butterfly"></div>
    <div class="photo photo--path" role="img" aria-label="Photo of a curving garden path lined with red begonias and lime green plants"></div>
  </section>

  <section class="side side--back">
    <div class="brand">
      <span class="brand__name">Tom Brenner<br>Garden Design</span>
      <span class="brand__dot"></span>
    </div>
    <p class="back__note">Find some of our completed designs<br>at YardCraft on Gardenly<br>or yardcraft.example</p>
    <div class="divider"></div>
    <div class="call-band">
      <span class="call-band__phone">(555) 316-2087</span>
    </div>
    <p class="tagline">Allow us to transform your home into a custom paradise.<br>We strive to please YOU!</p>
  </section>
</body>
</html>
```